Business card design needed with water logo.

I have already designed a card at Cardlyne, but prepared to pay $139 as advertised for a more professional look.
I presume it will then be available to me to order through Card Lyne?
The Website address needs to be large font.
I sell light weight water features at shopping centres to the public but at wholesale prices.
Need a card that is EASY TO READ, as go through literally thousands of cards as customer pick them up from my display stand.
The current logo I use is the Card Lyne Pebblemark.
PLEASE PLACE ALL INFORMATION THAT I HAVE PROVIDED ON THE CARD
Designers keep missing out my requirements

Target Market(s)

Retail prospective customers who walk by and take a card for future reference. I go through thousands of cards so economical is a must

Industry/Entity Type

Shopping

Contact Information for Business Card

StoneFlow Company
W.A. Wholesale Agent for Rockspouts QLD
Light Weight Fibre Glass Water Features
www.rockspoutsonline.com.au
See website for products but listed are RETAIL Prices
contact
MAREN TOWSLEY
for WA Wholesale Direct Pricing
Ph: 0428596317 email: stoneflowco@brinkmail.net.au

BACK OF CARD to Read.
Stoneflow Company DISPLAYS ONLY AT SHOPPING CENTRES
..........................................................................
.........................................................................
WAREHOUSE STORAGE ONLY ( No Display)
KESTRELWAY FREIGHT
14 Pardoe Rd, Brantwick WA 6190 ABN 58209364172

Logo Text

StoneFlow Company

Logo styles of interest
Pictorial/Combination Logo
Requirements
Must have
• Large font to be easy to read, ALL INFORMATION On, that I specified.
This information is from my own designed card and I require the same Information just in a more professional format.

```html
<!DOCTYPE html>
<html lang="en">
<head>
<meta charset="utf-8">
<title>StoneFlow Company – Business Card</title>
<link href="https://fonts.googleapis.com/css2?family=Open+Sans:wght@400;600;700&display=swap" rel="stylesheet">
<style>
  :root {
    --bg: #2a2a2c;
    --navy: #123a63;
    --navy-deep: #0d2c4d;
    --blue: #2a8fd0;
    --blue-mid: #3e6e9c;
    --ink: #1d2530;
    --pale: #eef2f6;
    --pale-blue: #d3dde7;
    --band-text: #e4e9ee;
    --grey: #6d6f72;
    --grey-light: #9a9c9f;
    --paper: #f6f6f6;
  }
  * { box-sizing: border-box; margin: 0; padding: 0; }
  html, body {
    width: 1200px; height: 900px; overflow: hidden;
    background: var(--bg);
    font-family: "Open Sans", Arial, sans-serif;
  }
  .canvas { position: relative; width: 1200px; height: 900px; }

  .card {
    position: absolute; width: 620px; height: 354px;
    overflow: hidden; border-radius: 3px;
    box-shadow: 0 10px 30px rgba(0,0,0,.45);
  }

  /* ---------- Back ---------- */
  .card-back { left: 90px; top: 60px; background: var(--paper); color: var(--grey); }
  .card-back .brand-mark {
    position: absolute; left: 36px; top: 200px; width: 110px; height: 80px;
    background: var(--grey);
  }
  .card-back .brand-name {
    position: absolute; left: 190px; top: 26px;
    font-size: 46px; font-weight: 700; line-height: 1; color: var(--grey);
  }
  .card-back .brand-name span {
    display: block; font-size: 16px; letter-spacing: 18px; margin: 8px 0 0 40px;
  }
  .card-back .displays {
    position: absolute; left: 190px; top: 122px;
    font-size: 14px; font-weight: 600; letter-spacing: .5px;
  }
  .card-back .write-lines { position: absolute; left: 190px; top: 160px; width: 390px; }
  .card-back .write-lines li {
    list-style: none; height: 26px; border-bottom: 1px dotted var(--grey-light);
  }
  .card-back .warehouse {
    position: absolute; left: 190px; top: 272px;
    font-size: 12px; line-height: 1.45; font-weight: 600;
  }
  .card-back .abn {
    position: absolute; right: 28px; bottom: 22px; font-size: 10px;
  }

  /* ---------- Front ---------- */
  .card-front {
    left: 490px; top: 480px;
    background: linear-gradient(160deg, #ffffff 0%, var(--pale) 55%, var(--pale-blue) 100%);
    color: var(--ink);
  }
  .card-front .tab {
    position: absolute; right: -12px; top: 54px; width: 54px; height: 90px;
    background: var(--navy); border-radius: 10px;
  }
  .card-front .brand-mark {
    position: absolute; left: 30px; top: 64px; width: 100px; height: 72px;
    background: var(--blue);
  }
  .card-front .brand-name {
    position: absolute; left: 170px; top: 26px;
    font-size: 46px; font-weight: 700; line-height: 1; color: var(--navy);
  }
  .card-front .brand-name span {
    display: block; font-size: 15px; letter-spacing: 20px; margin: 10px 0 0 60px;
  }
  .card-front .agent {
    position: absolute; right: 52px; top: 108px; text-align: right;
    font-size: 13px; font-weight: 700; line-height: 1.3;
  }
  .card-front .agent p + p { margin-top: 12px; }
  .card-front .contact { position: absolute; left: 30px; top: 142px; }
  .card-front .intro { font-size: 12px; font-weight: 600; line-height: 1.25; }
  .card-front .person {
    font-size: 27px; font-weight: 400; color: var(--blue); line-height: 1.1; letter-spacing: .5px;
  }
  .card-front .pricing { font-size: 12px; font-weight: 600; }
  .card-front .lines { margin-top: 8px; font-size: 13px; line-height: 1.45; }
  .card-front .lines b { color: var(--blue); font-weight: 700; }
  .card-front .band {
    position: absolute; left: 0; right: 0; bottom: 0; height: 72px;
    background: linear-gradient(180deg, var(--blue-mid) 0%, var(--navy) 45%, var(--navy-deep) 100%);
  }
  .card-front .website {
    position: absolute; left: 0; right: 0; bottom: 14px; text-align: center;
    font-size: 33px; font-weight: 700; color: var(--band-text); letter-spacing: .5px; line-height: 1.3;
  }
</style>
</head>
<body>
<main class="canvas">

  <section class="card card-back" aria-label="Business card back">
    <div class="brand-mark"></div>
    <h2 class="brand-name">StoneFlow<span>COMPANY</span></h2>
    <p class="displays">DISPLAYS ONLY AT SHOPPING CENTRES</p>
    <ul class="write-lines"><li></li><li></li><li></li><li></li></ul>
    <p class="warehouse">WAREHOUSE STORAGE ONLY (No Display)<br>KESTRELWAY FREIGHT<br>14 Pardoe Rd, Brantwick WA 6190</p>
    <p class="abn">ABN 58209364172</p>
  </section>

  <section class="card card-front" aria-label="Business card front">
    <div class="tab"></div>
    <div class="brand-mark"></div>
    <h1 class="brand-name">StoneFlow<span>COMPANY</span></h1>
    <div class="agent">
      <p>W.A. Wholesale Agent<br>for Rockspouts</p>
      <p>QLD Light Weight Fibre<br>Glass Water Features</p>
    </div>
    <div class="contact">
      <p class="intro">See website for products<br>but listed are RETAIL Prices contact</p>
      <p class="person">MAREN TOWSLEY</p>
      <p class="pricing">for WA Wholesale Direct Pricing</p>
      <p class="lines"><b>P:</b> 0428 596 317<br><b>E:</b> stoneflowco@brinkmail.net.au</p>
    </div>
    <div class="band"></div>
    <p class="website">www.rockspoutsonline.com.au</p>
  </section>

</main>
</body>
</html>
```